Design a New Business Card for Our Company

We are looking for fresh, unique, and a modern business card that reflects our roots as digital marketing agency focused on SEM.

Industry/Entity Type

Marketing

Contact Information for Business Card

looking for very unique out of the box designs. clean and modern that compliments our logo

Requirements
Must have
• colors should match our logo
• Front should have name, address, email, and phone/fax of the person, phone/fax are the same number
• back should have our url

```html
<!DOCTYPE html>
<html lang="en">
<head>
<meta charset="utf-8">
<title>Brightpath Solutions Business Card</title>
<link rel="stylesheet" href="https://fonts.googleapis.com/css2?family=Arimo:wght@400;700&display=swap">
<style>
  :root {
    --backdrop: #3b3430;
    --card: #1c1c1d;
    --card-edge: #2a2a2b;
    --blue: #5b97d6;
    --grey: #c9c9c9;
    --white: #f2f2f2;
    --divider: #6c6c6c;
  }
  * { margin: 0; padding: 0; box-sizing: border-box; }
  html, body {
    width: 1200px;
    height: 787px;
    overflow: hidden;
    background: var(--backdrop);
    font-family: "Arimo", Arial, sans-serif;
  }
  .stage {
    position: relative;
    width: 1200px;
    height: 787px;
  }
  .card {
    position: absolute;
    top: 243px;
    width: 525px;
    height: 300px;
    background: var(--card);
    border: 1px solid var(--card-edge);
    border-radius: 3px;
    box-shadow: 0 10px 30px rgba(0,0,0,0.45);
  }
  /* Back side */
  .card-back { left: 50px; }
  .brand {
    position: absolute;
    left: 70px;
    top: 100px;
    display: flex;
    align-items: center;
    gap: 16px;
  }
  .brand-dot {
    width: 44px;
    height: 44px;
    border-radius: 50%;
    background: var(--blue);
  }
  .brand-name {
    font-size: 40px;
    font-weight: 700;
    color: var(--blue);
    letter-spacing: -0.5px;
  }
  .website {
    position: absolute;
    left: 74px;
    top: 205px;
    font-size: 15px;
    color: var(--white);
    letter-spacing: 6px;
  }
  /* Front side */
  .card-front { left: 625px; }
  .mark {
    position: absolute;
    left: 62px;
    top: 92px;
    width: 110px;
    height: 110px;
    border-radius: 50%;
    background: var(--blue);
  }
  .divider {
    position: absolute;
    left: 222px;
    top: 52px;
    width: 1px;
    height: 196px;
    background: linear-gradient(to bottom, transparent, var(--divider) 20%, var(--divider) 80%, transparent);
  }
  .details {
    position: absolute;
    left: 248px;
    top: 64px;
    color: var(--white);
  }
  .person-name {
    font-size: 20px;
    font-weight: 700;
    color: var(--grey);
  }
  .person-title {
    font-size: 17px;
    color: var(--blue);
    margin-top: 3px;
  }
  .address {
    font-size: 16px;
    line-height: 21px;
    margin-top: 12px;
  }
  .contact-list {
    list-style: none;
    margin-top: 6px;
  }
  .contact-list li {
    display: flex;
    align-items: center;
    gap: 10px;
    font-size: 16px;
    line-height: 23px;
  }
  .contact-icon {
    width: 16px;
    height: 14px;
    fill: var(--grey);
    flex: none;
  }
</style>
</head>
<body>
<main class="stage">
  <section class="card card-back" aria-label="Card back">
    <div class="brand">
      <span class="brand-dot"></span>
      <span class="brand-name">Brightpath Solutions</span>
    </div>
    <p class="website">www.example.com</p>
  </section>

  <section class="card card-front" aria-label="Card front">
    <div class="mark"></div>
    <div class="divider"></div>
    <div class="details">
      <p class="person-name">Mara Quill</p>
      <p class="person-title">President</p>
      <p class="address">2716 Harbor Lane<br>Oak Ridge, NY 10452</p>
      <ul class="contact-list">
        <li>
          <svg class="contact-icon" viewBox="0 0 16 14" aria-label="Phone"><path d="M1 4c0-2 3-3 7-3s7 1 7 3v1h-4V4H5v1H1z M3 6h10l2 7H1z"/></svg>
          555 0142 7781
        </li>
        <li>
          <svg class="contact-icon" viewBox="0 0 16 14" aria-label="Fax"><rect x="4" y="0" width="8" height="5"/><rect x="1" y="5" width="14" height="8" rx="1"/></svg>
          555 0198 3340
        </li>
        <li>
          <svg class="contact-icon" viewBox="0 0 16 14" aria-label="Email"><path d="M1 2h14v10H1z M2 3l6 5 6-5" fill="none" stroke="#c9c9c9" stroke-width="1.5"/></svg>
          mara@example.com
        </li>
      </ul>
    </div>
  </section>
</main>
</body>
</html>
```